Electrical company business card design.

Hi, were an electrical company in Auckland New Zealand called Quarneth Ltd. We focus mainly on high end residential and commercial so the card would be targeted towards that.
The card will be for myself, i am the director of the company.
Name: Derek Olstow
Position: Director/electrician
Phone: 021 387 9415
Email: derek@quarneth.co.nz
Location: Auckland
As for colors the the blue color in the logo is preferred, i also don't mind a black background option.
Target Market(s)
High end residential and commercial
Industry/Entity Type
Electrician
Contact Information for Business Card
Name: Derek Olstow Position: Director/Electrician Phone: 021 387 9415, Email: derek@quarneth.co.nz, Location: Auckland

```html
<!DOCTYPE html>
<html lang="en">
<head>
<meta charset="utf-8">
<title>Quarneth Ltd — Business Card</title>
<link href="https://fonts.googleapis.com/css2?family=Roboto:wght@400;500;700&display=swap" rel="stylesheet">
<style>
  :root {
    --stage: #3d3d3f;
    --card-black: #1c1c1e;
    --card-black-edge: #111113;
    --steel: #b9bcc1;
    --steel-dim: #8d9096;
    --blue-deep: #0a3f6e;
    --blue-mid: #105a8c;
    --blue-bright: #1e82d6;
    --white: #ffffff;
    --rule: rgba(255, 255, 255, 0.85);
  }
  * { box-sizing: border-box; margin: 0; padding: 0; }
  html, body {
    width: 1200px;
    height: 694px;
    overflow: hidden;
    background: var(--stage);
    font-family: "Roboto", Arial, sans-serif;
  }
  .canvas {
    position: relative;
    width: 1200px;
    height: 694px;
  }
  .card {
    position: absolute;
    top: 190px;
    width: 520px;
    height: 316px;
    border-radius: 26px;
    overflow: hidden;
    box-shadow: 0 18px 40px rgba(0, 0, 0, 0.45);
  }

  /* Front */
  .card-front {
    left: 50px;
    background: linear-gradient(145deg, var(--card-black) 0%, var(--card-black-edge) 100%);
    display: flex;
    align-items: center;
    justify-content: center;
  }
  .brand {
    display: flex;
    flex-direction: column;
    align-items: flex-start;
  }
  .brand-row {
    display: flex;
    align-items: center;
    gap: 16px;
  }
  .brand-square {
    width: 40px;
    height: 40px;
    background: var(--blue-bright);
  }
  .brand-name {
    font-size: 62px;
    font-weight: 500;
    letter-spacing: 2px;
    color: var(--steel);
    line-height: 1;
    text-transform: uppercase;
  }
  .brand-tagline {
    margin-top: 10px;
    margin-left: 56px;
    font-size: 17px;
    font-weight: 700;
    letter-spacing: 2.5px;
    color: var(--steel-dim);
    text-transform: uppercase;
  }

  /* Back */
  .card-back {
    left: 630px;
    background: radial-gradient(ellipse at 70% 10%, var(--blue-mid) 0%, var(--blue-deep) 75%);
    color: var(--white);
  }
  .rule {
    position: absolute;
    left: 40px;
    right: 40px;
    height: 1px;
    background: var(--rule);
  }
  .rule-top { top: 36px; }
  .rule-mid { top: 118px; }
  .rule-bottom { top: 206px; }
  .person {
    position: absolute;
    top: 52px;
    left: 0;
    right: 0;
    text-align: center;
  }
  .person-name {
    font-size: 34px;
    font-weight: 500;
    line-height: 1.05;
  }
  .person-role {
    margin-top: 4px;
    font-size: 10px;
    letter-spacing: 3px;
    text-transform: uppercase;
  }
  .contact {
    position: absolute;
    top: 130px;
    left: 0;
    right: 0;
    text-align: center;
  }
  .contact-label {
    display: inline-flex;
    align-items: center;
    gap: 6px;
    font-size: 11px;
    letter-spacing: 4px;
    text-transform: uppercase;
  }
  .contact-label svg { width: 13px; height: 13px; fill: var(--white); }
  .contact-phone {
    font-size: 48px;
    font-weight: 500;
    letter-spacing: 1px;
    line-height: 1.1;
  }
  .location {
    position: absolute;
    top: 218px;
    left: 0;
    right: 0;
    display: flex;
    flex-direction: column;
    align-items: center;
  }
  .location-landmark {
    width: 34px;
    height: 52px;
    background: linear-gradient(180deg, rgba(255,255,255,0.9), rgba(255,255,255,0.55));
    border-radius: 4px;
  }
  .location-name {
    margin-top: 12px;
    font-size: 13px;
    letter-spacing: 7px;
    text-transform: uppercase;
  }
</style>
</head>
<body>
<main class="canvas">
  <section class="card card-front" aria-label="Card front">
    <div class="brand">
      <div class="brand-row">
        <span class="brand-square"></span>
        <span class="brand-name">Quarneth</span>
      </div>
      <span class="brand-tagline">Power meets precision</span>
    </div>
  </section>

  <section class="card card-back" aria-label="Card back">
    <div class="rule rule-top"></div>
    <div class="person">
      <div class="person-name">Derek Olstow</div>
      <div class="person-role">Director/Electrician</div>
    </div>
    <div class="rule rule-mid"></div>
    <div class="contact">
      <div class="contact-label">
        <svg viewBox="0 0 24 24" aria-hidden="true"><path d="M6.6 10.8a15.1 15.1 0 0 0 6.6 6.6l2.2-2.2a1 1 0 0 1 1-.25 11.4 11.4 0 0 0 3.6.57 1 1 0 0 1 1 1V20a1 1 0 0 1-1 1A17 17 0 0 1 3 4a1 1 0 0 1 1-1h3.5a1 1 0 0 1 1 1c0 1.25.2 2.45.57 3.6a1 1 0 0 1-.25 1z"/></svg>
        Phone
      </div>
      <div class="contact-phone">021 387 9415</div>
    </div>
    <div class="rule rule-bottom"></div>
    <div class="location">
      <div class="location-landmark" role="img" aria-label="Line illustration of the Auckland city tower"></div>
      <div class="location-name">Auckland</div>
    </div>
  </section>
</main>
</body>
</html>
```